Package design for quilted mattress covers.

We are producing a comfortable "quilted mattress protector" for beds . We need a very elegant and attractive and cozy insert label. approx. size is 14 inches high x11 inches wide. (One base design with slight edits to customize for each different bed size) It will be packaged in a nice clear bag, with the design label in front. I attached the type of product for reference

package text:
QUILTED MATTRESS COVER

size: 33x75x10"

*ultimate comfort
*breathable cotton top
*waterproof lining
*easy care wash and dry

Target Market(s)

displayed in drygood and bedding retail stores

Colors

Designer to choose colors to be used in the design.

Requirements
Must have
• all info as in description
Nice to have
• an image of a quilted cover on a bed, professionally included in the package design
Should not have
• ..

```html
<!DOCTYPE html>
<html lang="en">
<head>
<meta charset="utf-8">
<title>Lumora Quilted Mattress Cover – Package Label</title>
<link rel="stylesheet" href="https://fonts.googleapis.com/css2?family=Cinzel:wght@700;800&display=swap">
<style>
  :root {
    --navy: #3b4b7d;
    --navy-shadow: rgba(40, 50, 90, 0.35);
    --ink: #2e2e33;
    --accent-red: #c8201e;
    --paper: #f4f4f6;
    --wash-light: #fbfbfc;
    --wash-mid: #dcdde1;
    --wash-dark: #b9bbc1;
    --photo-light: #f2efea;
    --photo-mid: #dcd6cc;
    --photo-dark: #bfb8ac;
    --frame: #4a4a4a;
  }
  * { margin: 0; padding: 0; box-sizing: border-box; }
  html, body { width: 943px; height: 1200px; overflow: hidden; background: #ffffff; }
  .label {
    position: relative;
    width: 943px;
    height: 1200px;
    overflow: hidden;
    border: 2px solid var(--frame);
    font-family: "Cinzel", serif;
  }
  .label__backdrop {
    position: absolute;
    inset: 0;
    background:
      radial-gradient(ellipse 60% 40% at 15% 20%, var(--wash-mid), transparent 70%),
      radial-gradient(ellipse 50% 45% at 85% 30%, var(--wash-dark), transparent 70%),
      radial-gradient(ellipse 55% 35% at 20% 80%, var(--wash-mid), transparent 70%),
      radial-gradient(ellipse 50% 40% at 85% 85%, var(--wash-mid), transparent 70%),
      var(--wash-light);
  }
  .brand {
    position: absolute;
    left: 0;
    right: 0;
    top: 210px;
    text-align: center;
    font-weight: 800;
    font-size: 104px;
    line-height: 1;
    color: var(--navy);
    letter-spacing: 2px;
  }
  .product-photo {
    position: absolute;
    left: 155px;
    top: 360px;
    width: 638px;
    height: 508px;
    background:
      linear-gradient(180deg, var(--photo-mid) 0%, var(--photo-light) 30%, #ffffff 55%, #f1f1f3 80%, var(--photo-dark) 100%);
  }
  .product-title {
    position: absolute;
    left: 0;
    right: 0;
    top: 898px;
    text-align: center;
    font-weight: 700;
    font-size: 45px;
    letter-spacing: 0.5px;
    color: var(--navy);
    text-shadow: 2px 2px 2px var(--navy-shadow);
  }
  .features {
    position: absolute;
    left: 57px;
    top: 1040px;
    list-style: none;
    font-weight: 700;
    font-size: 19px;
    line-height: 27px;
    color: var(--ink);
    text-transform: uppercase;
  }
  .size-spec {
    position: absolute;
    left: 667px;
    top: 1115px;
    font-weight: 700;
    font-size: 20px;
    color: var(--accent-red);
    text-transform: uppercase;
  }
</style>
</head>
<body>
  <main class="label">
    <div class="label__backdrop" role="img" aria-label="Soft grey watercolour feather texture background"></div>
    <div class="brand">Lumora</div>
    <div class="product-photo" role="img" aria-label="Photo of a bed dressed with a white quilted mattress cover, pillows and a vase of flowers"></div>
    <h1 class="product-title">QUILTED MATTRESS COVER</h1>
    <ul class="features">
      <li>*Ultimate comfort</li>
      <li>*Breathable cotton top</li>
      <li>*Waterproof lining</li>
      <li>*Easy care wash and dry</li>
    </ul>
    <p class="size-spec">Size: 33x75x10”</p>
  </main>
</body>
</html>
```